Graphics for Vorlani telehealth weight loss plans

Vorlani focuses on delivering medical weight-loss using prescription medicine and telehealth consults. Vorlani needs graphics for its ecommerce site for three weight loss plans. The plans are posted here with current graphics and descriptions of what is included with each plan. Please do not feel constrained by current graphics or styling.

- https://shop.vorlanicare.com/products/steady-horizon-plan
- https://shop.vorlanicare.com/products/amber-ridge-plan
- https://shop.vorlanicare.com/products/calm-harbor-plan

The graphics need to look good on mobile and desktop browsers.

```html
<!DOCTYPE html>
<html lang="en">
<head>
<meta charset="utf-8">
<title>Vorlani Weight Loss Plans</title>
<link href="https://fonts.googleapis.com/css2?family=Oswald:wght@400;500;600;700&family=Source+Sans+3:wght@400;600;700&display=swap" rel="stylesheet">
<style>
:root{
  --cyan:#27cdfd;
  --navy:#26215e;
  --ink-navy:#221f5f;
  --royal:#2c4fa6;
  --accent-cyan:#2fcdf8;
  --white:#ffffff;
  --black:#111111;
  --photo-light:#c9c9c9;
  --photo-dark:#5e5e5e;
}
*{margin:0;padding:0;box-sizing:border-box}
html,body{width:1200px;height:749px;overflow:hidden;background:var(--white)}
body{position:relative;font-family:"Source Sans 3",Arial,sans-serif;color:var(--black)}
.plan{position:absolute;top:16px;width:339px}
.plan--amber{left:88px}
.plan--calm{left:439px}
.plan--steady{left:790px}
.plan-art{position:relative;width:339px;height:439px;overflow:hidden;font-family:"Oswald",sans-serif}
.plan--amber .plan-art{background:var(--cyan);color:var(--ink-navy)}
.plan--calm .plan-art{background:var(--navy);color:var(--accent-cyan)}
.plan--steady .plan-art{background:var(--royal);color:var(--white)}
.plan-photo{position:absolute;left:0;top:0;width:339px;height:140px;
  clip-path:polygon(0 0,100% 0,100% 140px,260px 140px,260px 96px,0 96px);
  background:linear-gradient(120deg,var(--photo-dark) 0%,var(--photo-light) 45%,#e2e2e2 70%,#8d8d8d 100%)}
.plan-title{position:absolute;left:23px;top:104px;font-weight:700;font-size:38px;line-height:39px;text-transform:uppercase;letter-spacing:-.2px;white-space:nowrap}
.plan--calm .plan-title{left:22px;top:104px;font-size:35px;line-height:38px}
.plan--steady .plan-title{left:21px;top:105px;font-size:34px;line-height:38px}
.plan-sub{position:absolute;left:23px;font-weight:400;font-size:18px;line-height:21px;text-transform:uppercase}
.plan--amber .plan-sub{top:182px}
.plan--steady .plan-sub{left:25px;top:187px;font-size:17.5px}
.includes{position:absolute;left:23px;height:19px;padding:0 6px;font-size:12.5px;font-weight:500;line-height:19px;border-radius:1px}
.plan--amber .includes{top:234px;background:var(--ink-navy);color:var(--white)}
.plan--calm .includes{left:23px;top:191px;background:var(--accent-cyan);color:var(--navy)}
.plan--steady .includes{left:26px;top:239px;background:var(--white);color:var(--ink-navy)}
.features{position:absolute;list-style:none;font-weight:500;font-size:13px;line-height:15px}
.features li{position:relative;padding-left:8px;margin-bottom:8px}
.features li::before{content:"•";position:absolute;left:0;top:0}
.features small{display:block;font-weight:400;font-size:9.5px;line-height:12px}
.features .note{font-weight:400;font-size:10px}
.plan--amber .features--left{left:19px;top:261px;width:125px}
.plan--amber .features--right{left:153px;top:258px;width:180px}
.plan--amber .features--right li{margin-bottom:11px}
.plan--calm .features{left:19px;top:228px;width:310px;font-size:13.5px}
.plan--calm .features li{margin-bottom:12px}
.plan--calm .features small{display:inline;font-size:10px;margin-left:3px}
.plan-note{position:absolute;left:22px;top:332px;font-size:10px;font-weight:400;color:var(--accent-cyan)}
.plan--steady .features--left{left:19px;top:268px;width:142px}
.plan--steady .features--right{left:162px;top:267px;width:172px}
.plan--steady .features li{margin-bottom:7px}
.pay{position:absolute;top:374px;display:flex;align-items:center}
.plan--amber .pay{left:22px}
.plan--calm .pay{left:25px}
.plan--steady .pay{left:22px}
.pay-icon{width:38px;height:38px;border-radius:50%;display:flex;align-items:center;justify-content:center;position:relative;z-index:1}
.pay-label{margin-left:-4px;height:19px;padding:0 10px 0 14px;font-size:11.5px;font-weight:500;line-height:19px}
.plan--amber .pay-icon,.plan--amber .pay-label{background:var(--ink-navy);color:var(--white)}
.plan--calm .pay-icon,.plan--calm .pay-label{background:var(--accent-cyan);color:var(--navy)}
.plan--steady .pay-icon,.plan--steady .pay-label{background:var(--white);color:var(--ink-navy)}
.plan-name{margin:21px 0 0 1px;font-weight:700;font-size:25px;line-height:35px;letter-spacing:.3px}
.plan--steady .plan-name{margin-left:6px}
.plan-price{margin:9px 0 0 1px;font-size:20px;line-height:26px;letter-spacing:.5px}
.plan--steady .plan-price{margin-left:6px}
.plan-buy{display:block;margin-top:14px;width:333px;height:66px;background:var(--black);color:var(--white);
  font-size:20px;line-height:66px;text-align:center;text-decoration:none;letter-spacing:1px}
.plan--calm .plan-buy{margin-left:3px}
.plan--steady .plan-buy{margin-left:5px}
.discount{position:absolute;left:27px;top:659px;width:199px;height:65px;border-radius:10px;background:#000;color:var(--white);
  font-family:Arial,Helvetica,sans-serif;font-size:20px;line-height:65px;text-align:center}
</style>
</head>
<body>

<article class="plan plan--amber">
  <div class="plan-art">
    <div class="plan-photo" role="img" aria-label="Black and white photo of a measuring tape around a waist with capsules"></div>
    <h2 class="plan-title">Amber Ridge<br>Plan</h2>
    <p class="plan-sub">Physician Consultation<br>Phentermine Program</p>
    <span class="includes">Includes</span>
    <ul class="features features--left">
      <li>100% online.<small>No need to visit the office.</small></li>
      <li>Phentermine prescription.</li>
      <li>Medical consultation.</li>
    </ul>
    <ul class="features features--right">
      <li>Real Phentermine <span class="note">(37.5mg/Pill)</span> delivered to your door.</li>
      <li>1 month supply. <span class="note">(30 pills)</span></li>
      <li>FREE Introductory Nutritionist consult on your first month.</li>
    </ul>
    <div class="pay">
      <span class="pay-icon"><svg width="24" height="24" viewBox="0 0 24 24" fill="none" stroke="currentColor" stroke-width="1.6"><circle cx="12" cy="10" r="6"/><path d="M12 6.5v7M10 8.5h3a1 1 0 0 1 0 2h-2a1 1 0 0 0 0 2h3"/><path d="M4 13a8 8 0 0 0 14 5M18 18l0-3M18 18h-3"/></svg></span>
      <span class="pay-label">Month-to-month pay as you go.</span>
    </div>
  </div>
  <h3 class="plan-name">Amber Ridge Plan</h3>
  <p class="plan-price">$119.00</p>
  <a class="plan-buy" href="https://shop.vorlanicare.com/products/amber-ridge-plan">View details and buy</a>
</article>

<article class="plan plan--calm">
  <div class="plan-art">
    <div class="plan-photo" role="img" aria-label="Black and white photo of a woman in a sports top holding a shaker bottle"></div>
    <h2 class="plan-title">Calm Harbor<br>Plan</h2>
    <span class="includes">Includes</span>
    <ul class="features">
      <li>100% online.<small>No need to visit the office.</small></li>
      <li>Expert nutrition consult.</li>
      <li>Custom crafted diet plan to achieve your goals.</li>
      <li>Nutrition coaching to improve your health and vitality.</li>
    </ul>
    <p class="plan-note">*Does not include medication</p>
    <div class="pay">
      <span class="pay-icon"><svg width="24" height="24" viewBox="0 0 24 24" fill="none" stroke="currentColor" stroke-width="1.6"><circle cx="12" cy="10" r="6"/><path d="M12 6.5v7M10 8.5h3a1 1 0 0 1 0 2h-2a1 1 0 0 0 0 2h3"/><path d="M4 13a8 8 0 0 0 14 5M18 18l0-3M18 18h-3"/></svg></span>
      <span class="pay-label">Month-to-month pay as you go.</span>
    </div>
  </div>
  <h3 class="plan-name">Calm Harbor Plan</h3>
  <p class="plan-price">$99.00</p>
  <a class="plan-buy" href="https://shop.vorlanicare.com/products/calm-harbor-plan">View details and buy</a>
</article>

<article class="plan plan--steady">
  <div class="plan-art">
    <div class="plan-photo" role="img" aria-label="Black and white photo of an athletic torso with capsules"></div>
    <h2 class="plan-title">Steady Horizon<br>Plan</h2>
    <p class="plan-sub">Physician Consultation<br>Phentermine Program</p>
    <span class="includes">Includes</span>
    <ul class="features features--left">
      <li>100% online.<small>No need to visit the office.</small></li>
      <li>1 month supply. <span class="note">(30 pills)</span></li>
      <li>Custom crafted diet plan to achieve your goals.</li>
    </ul>
    <ul class="features features--right">
      <li>Real Phentermine <span class="note">(37.5mg/Pill)</span> delivered to your door.</li>
      <li>Expert nutrition consult.</li>
      <li>Nutrition coaching to improve your health and vitality.</li>
    </ul>
    <div class="pay">
      <span class="pay-icon"><svg width="24" height="24" viewBox="0 0 24 24" fill="none" stroke="currentColor" stroke-width="1.6"><circle cx="12" cy="10" r="6"/><path d="M12 6.5v7M10 8.5h3a1 1 0 0 1 0 2h-2a1 1 0 0 0 0 2h3"/><path d="M4 13a8 8 0 0 0 14 5M18 18l0-3M18 18h-3"/></svg></span>
      <span class="pay-label">Month-to-month pay as you go.</span>
    </div>
  </div>
  <h3 class="plan-name">Steady Horizon<br>Plan</h3>
  <p class="plan-price">$199.00</p>
  <a class="plan-buy" href="https://shop.vorlanicare.com/products/steady-horizon-plan">View details and buy</a>
</article>

<div class="discount">GET 10% OFF</div>

</body>
</html>
```